Website design for an Online pastry shop

Website Name : www.lanternandplum.example

Description of the website and its target audience
We are a premium pastry company producing delicious cakes, macarons, cookies, gelato, and other sweet dessert. Our differentiation is that our products are freshly produced with premium quality imported ingredients and one bite into our products set us apart from other bakery shop. We online retail online so as to provide high quality products at a affordable cost. Our products has received raving reviews by many food enthusiast even the hard to please ones. The products contain more natural ingredients and we do not add preservatives. The return rates for our pastry is almost 80%. You only need to try once to be return customers. Our greatest challenge is getting customer to take the first bite. We are so sure of our products that we are going to give people free food tasting.

We are based in China but all our products are developed by award winning chefs from 5 stars hotel. The target customer is woman 16 to 40+ in china. Working class ladies and demand high quality products. A modern, sophisticated and minimalist website

This is a competitive market and image is crucial for such a food ‘conscious ’ orientated customer. They want to feel that they are buying from a reliable company that take great effort to ensure food cleaniness and safety yet affordable price. We make almost 98% of sub ingredients ourselves and we make it by hand.

Style/theme ideas for the web page design
I am looking for a elegant a little rustic, handmade feel yet sophisticated design - one that is easy to the eye yet functional and easy for the user to navigate through. Good play of fonts to give let it feel unique and customised. Black and white is our corporate colours. However, we do not want black background as it does not tease the taste bud. All our colours should come from our products. Customers should be very close to our products. They eat with their eyes first. Black and white is just accent.

Inspirational and competitors websites
http://www.47tart.example/ ( Key competitor )
I like the simple, clean look. The products are the key focus
https://www.pelvora.example/
clean, fresh and different. Attractive with purpose. Feminine
http://moatandwillow.example/
this has a great layout - lots of information and nicely presented. Very sweet and feminine
http://www.storeharbourly.example/
product features is the focus
http://www.janetobrill.example/store/
fun, feminine, rustic

Number of pages needed : 6 ( Uncoded PSD design only )
Page descriptions
Home Page - This page will show what makes our products stand out from the competitors and provide an introduction of who we are.
2nd page : Product catalogue
3nd page: Detail Product page with pictures and descriptions. Select products size and add to cart....
4rd page: Brand Story with pictures and descriptions.
5th page Contact Us : Here they can contact or schedule an appointment for free product tasting
6th page : Check out page

• Please see the project wire frame file " main page.png " or file number 70

```html
<!DOCTYPE html>
<html lang="en">
<head>
<meta charset="utf-8">
<title>Lantern &amp; Plum — Pastry Cakes</title>
<link href="https://fonts.googleapis.com/css2?family=Josefin+Sans:wght@400;600&family=PT+Sans:wght@400;700&family=Ubuntu:wght@500&display=swap" rel="stylesheet">
<style>
:root{
  --ink:#1b1b1b;
  --bar:#161616;
  --nav:rgba(40,38,36,.82);
  --white:#ffffff;
  --paper:#f2f1ef;
  --line:#bdbdbd;
  --text:#3a3a3a;
  --foot-box:#262626;
  --foot-edge:#3c3c3c;
  --btn:#2a2a2a;
}
*{margin:0;padding:0;box-sizing:border-box}
html,body{width:787px;height:1200px;overflow:hidden;background:var(--white)}
body{position:relative;font-family:"PT Sans",sans-serif;color:var(--text)}
.abs{position:absolute}
.topbar{left:0;top:0;width:787px;height:28px;background:var(--bar);color:#fff;font-size:8px;font-weight:700}
.topbar .promo{left:89px;top:9px}
.topbar .account{left:561px;top:9px;display:flex;gap:6px;align-items:center}
.hero{left:0;top:28px;width:787px;height:414px;
  background:linear-gradient(180deg,#7a5436 0%,#a8794f 22%,#d9cfc6 40%,#ece8e4 52%,#e2dbd4 62%,#c48a52 76%,#8e5e38 90%,#6c4a32 100%)}
.nav{left:0;top:28px;width:787px;height:70px;background:var(--nav)}
.nav a{position:absolute;top:26px;font-family:"Josefin Sans",sans-serif;font-size:8.5px;letter-spacing:2.6px;color:#e9e4de;text-decoration:none}
.brand{font-family:"Ubuntu",sans-serif;font-weight:500;color:#fff;text-align:center;white-space:nowrap}
.brand-dot{width:14px;height:14px;border-radius:50%;background:#fff}
.nav .brand{left:294px;width:200px;top:66px;font-size:12px}
.nav .brand-dot{left:387px;top:45px}
.hero-title{left:0;width:787px;top:262px;text-align:center;font-family:"Josefin Sans",sans-serif;font-weight:600;font-size:19px;letter-spacing:7px;color:#111}
.arrow{top:250px}
.intro-title{left:0;width:787px;top:473px;text-align:center;font-family:"Josefin Sans",sans-serif;font-weight:600;font-size:13px;letter-spacing:4px;color:#111}
.intro-text{left:0;width:787px;top:497px;text-align:center;font-size:10px;color:#444}
.featured{left:0;top:540px;width:787px;height:252px;background:var(--paper)}
.featured h2{position:absolute;left:0;width:787px;top:19px;text-align:center;font-family:"Josefin Sans",sans-serif;font-weight:600;font-size:13px;letter-spacing:4px;color:#111}
.featured .rule{position:absolute;left:73px;top:47px;width:641px;height:1px;background:var(--line)}
.product{position:absolute;top:65px;width:147px}
.product .photo{width:147px;height:133px}
.product span{display:block;margin-top:14px;font-size:10px;font-weight:700;color:#333}
.mailing{left:0;top:792px;width:787px;height:70px;background:#fff}
.mailing .label{left:74px;top:28px;font-size:10px;color:#222}
.mailing .field{left:182px;top:23px;width:220px;height:23px;background:#f6f6f6;border:1px solid #e6e6e6}
.mailing .subscribe{left:410px;top:23px;width:84px;height:23px;background:var(--btn);color:#fff;font-size:7.5px;font-weight:700;text-align:center;line-height:23px}
.mailing .follow{left:518px;top:28px;font-size:10px;color:#222}
.social{left:585px;top:25px;display:flex;gap:2px}
.social i{display:block;width:20px;height:20px;border-radius:50%}
.footer{left:0;top:862px;width:787px;height:338px;background:radial-gradient(ellipse at 40% 20%,#2a2a2a,#0b0b0b 75%)}
.menu{position:absolute;width:147px;height:59px;background:var(--foot-box);border:1px solid var(--foot-edge)}
.menu h3{height:18px;line-height:18px;padding-left:7px;font-size:8px;color:#fff;border-bottom:1px solid var(--foot-edge)}
.menu ul{list-style:none;padding:5px 7px;font-size:6px;color:#9a9a9a;line-height:12px}
.menu .scroll{position:absolute;right:1px;top:20px;width:4px;height:36px;border-left:1px solid var(--foot-edge)}
.pill{position:absolute;height:18px;line-height:17px;padding-left:7px;font-size:8px;font-weight:700;color:#fff;background:var(--foot-box);border:1px solid var(--foot-edge);white-space:nowrap}
.footer .brand{left:527px;width:200px;top:64px;font-size:12px}
.footer .brand-dot{left:620px;top:43px}
.promo-photo{left:566px;top:98px;width:148px;height:169px;
  background:linear-gradient(170deg,#5a4636 0%,#cfc3b2 30%,#efeae2 45%,#3a2546 62%,#2a1a36 75%,#d8c39a 90%,#ece6dc 100%)}
.footer .rule{left:0;top:296px;width:787px;height:1px;background:#222}
.copy{left:0;width:787px;top:311px;text-align:center;font-size:7px;color:#cfcfcf}
</style>
</head>
<body>

<div class="abs topbar">
  <div class="abs promo">Free Delivery &nbsp;For Order's Above $50</div>
  <div class="abs account">
    <span>Login</span><span>|</span><span>Sign Up</span>
    <svg width="8" height="9" viewBox="0 0 8 9"><rect x="0.5" y="3" width="7" height="6" fill="#fff"/><path d="M2 3.5V2a2 2 0 0 1 4 0v1.5" fill="none" stroke="#fff"/></svg>
    <span>Cart</span>
  </div>
</div>

<div class="abs hero" role="img" aria-label="Cream-topped pastry cake on a round wooden board, with a pastry basket and white teacup on a rustic table"></div>

<nav class="abs nav">
  <a style="left:114px">CAKES</a>
  <a style="left:176px">MACARONS</a>
  <a style="left:262px">COOKIES</a>
  <div class="abs brand-dot"></div>
  <div class="brand abs">Lantern &amp; Plum</div>
  <a style="left:437px">GELATO</a>
  <a style="left:507px">TASTING ROOM</a>
  <a style="left:616px">ABOUT US</a>
</nav>

<div class="abs hero-title">PASTRY CAKES</div>
<svg class="abs arrow" style="left:48px" width="16" height="26" viewBox="0 0 16 26"><path d="M14 1 2 13l12 12" fill="none" stroke="#fff" stroke-width="1.6"/></svg>
<svg class="abs arrow" style="left:726px" width="16" height="26" viewBox="0 0 16 26"><path d="M2 1l12 12L2 25" fill="none" stroke="#fff" stroke-width="1.6"/></svg>

<div class="abs intro-title">PASTRY CAKES</div>
<div class="abs intro-text">We Value flavour over fuss artisian, hard crated and other gourmet confections delivered direct to your door</div>

<section class="abs featured">
  <h2>FEATURED</h2>
  <div class="rule"></div>
  <div class="product" style="left:74px"><div class="photo" role="img" aria-label="Mango mousse cake topped with diced mango and mint" style="background:linear-gradient(180deg,#b9b0a6 0%,#d98a3a 30%,#f07a12 50%,#f0a53c 68%,#d8c3a4 85%,#cfc8be 100%)"></div><span>Cakes</span></div>
  <div class="product" style="left:238px"><div class="photo" role="img" aria-label="Single peach macaron on a white surface" style="background:linear-gradient(180deg,#f8f5f6 0%,#f4eef0 45%,#eab08c 58%,#f2e6e8 72%,#e9dde0 84%,#1c1418 90%,#151013 100%)"></div><span>Macarons</span></div>
  <div class="product" style="left:404px"><div class="photo" role="img" aria-label="Large cookie sandwich with cream and strawberry beside a teacup" style="background:linear-gradient(180deg,#7d8f7e 0%,#b99a74 25%,#efe9df 45%,#e6ddd0 60%,#b5846a 78%,#a06a3c 100%)"></div><span>Cookies</span></div>
  <div class="product" style="left:567px"><div class="photo" role="img" aria-label="Hands drizzling chocolate sauce over a cream tart" style="background:linear-gradient(180deg,#ede8e4 0%,#cfc3bb 30%,#e2d8e0 52%,#8a6c78 66%,#b88654 82%,#6b4a3a 100%)"></div><span>Gelato</span></div>
</section>

<section class="abs mailing">
  <div class="abs label">Join Our Mailing list box</div>
  <div class="abs field"></div>
  <div class="abs subscribe">SUBSCRIBE NOW !</div>
  <div class="abs follow">Follow Us :</div>
  <div class="abs social">
    <i style="background:#3b5a9a"></i><i style="background:#3fa9e0"></i><i style="background:#dc4a38"></i><i style="background:#1b7fbd"></i><i style="background:#3aa35a"></i><i style="background:#e12b28"></i>
  </div>
</section>

<footer class="abs footer">
  <div class="menu" style="left:73px;top:21px"><h3>Cakes</h3><ul><li>Mouse Cakes</li><li>Ice Cream Cakes</li></ul><div class="scroll"></div></div>
  <div class="menu" style="left:238px;top:21px"><h3>Gelato</h3><ul><li>Mouse Cakes</li><li>Ice Cream Cakes</li></ul><div class="scroll"></div></div>
  <div class="menu" style="left:402px;top:21px"><h3>Customer Service</h3><ul><li>Mouse Cakes</li><li>Ice Cream Cakes</li></ul><div class="scroll"></div></div>
  <div class="menu" style="left:73px;top:100px"><h3>Macarons</h3><ul><li>Mouse Cakes</li><li>Ice Cream Cakes</li></ul><div class="scroll"></div></div>
  <div class="menu" style="left:238px;top:100px"><h3>Cookies</h3><ul><li>Mouse Cakes</li><li>Ice Cream Cakes</li></ul><div class="scroll"></div></div>
  <div class="menu" style="left:402px;top:100px"><h3>About Us</h3><ul><li>Mouse Cakes</li><li>Ice Cream Cakes</li></ul><div class="scroll"></div></div>
  <div class="pill" style="left:73px;top:181px;width:147px">Questions ?</div>
  <div class="pill" style="left:73px;top:215px;width:147px;background:#000">Phone Number : -1-555-014-0177</div>
  <div class="pill" style="left:226px;top:215px;width:57px;padding-left:14px">E-Mail</div>
  <div class="pill" style="left:73px;top:247px;width:91px;padding-left:10px">Legal Informations</div>
  <div class="abs brand-dot"></div>
  <div class="brand abs">Lantern &amp; Plum</div>
  <div class="abs promo-photo" role="img" aria-label="Promotional panel: blueberry cheesecake on a white plate with a delicious cakes headline"></div>
  <div class="abs rule"></div>
  <div class="abs copy">© 2015 Company Name , All Rights Reserved</div>
</footer>

</body>
</html>
```